KVRo Business Cards

We need a business card design. We are a Technology (Audio Visual) design, sales and installation company. Looking for a double sided design, clean

Contact Information for Business Card

Clean, modern look, 2 sided

Font styles to use
Sans Serif

```html
<!DOCTYPE html>
<html lang="en">
<head>
<meta charset="UTF-8">
<title>KVRo Business Cards</title>
<link href="https://fonts.googleapis.com/css2?family=Poppins:wght@400;500;600;700&display=swap" rel="stylesheet">
<style>
  :root {
    --navy: #1b3040;
    --orange: #f39321;
    --white: #ffffff;
    --backdrop: #e9eaec;
    --rule: #4a4f55;
  }
  * { box-sizing: border-box; margin: 0; padding: 0; }
  html, body { width: 1200px; height: 900px; overflow: hidden; }
  body {
    background: var(--backdrop);
    font-family: "Poppins", sans-serif;
    display: flex;
    flex-direction: column;
    align-items: center;
    justify-content: center;
    gap: 40px;
  }
  .card {
    width: 560px;
    height: 320px;
    position: relative;
    box-shadow: 0 4px 14px rgba(0,0,0,0.12);
  }
  .card-front {
    background: var(--navy);
    display: flex;
    align-items: center;
    justify-content: center;
  }
  .wordmark {
    font-weight: 700;
    letter-spacing: 1px;
    line-height: 1;
  }
  .card-front .wordmark { color: var(--white); font-size: 92px; }
  .card-back { background: var(--white); }
  .card-back .wordmark {
    position: absolute;
    left: 48px;
    top: 92px;
    color: var(--navy);
    font-size: 60px;
  }
  .identity {
    position: absolute;
    right: 40px;
    top: 104px;
    text-align: right;
  }
  .person-name {
    font-size: 27px;
    font-weight: 600;
    line-height: 1.1;
  }
  .first-name { color: var(--orange); }
  .last-name { color: var(--navy); }
  .job-title {
    font-size: 13px;
    color: var(--navy);
    letter-spacing: 0.5px;
    margin-top: 2px;
  }
  .divider {
    position: absolute;
    left: 44px;
    right: 22px;
    top: 186px;
    border-top: 1px solid var(--rule);
  }
  .contact-list {
    position: absolute;
    left: 48px;
    top: 200px;
    list-style: none;
  }
  .contact-list li {
    display: flex;
    align-items: center;
    gap: 10px;
    font-size: 14px;
    color: var(--navy);
    line-height: 24px;
  }
  .contact-list svg, .address svg { width: 13px; height: 13px; flex: none; }
  .address {
    position: absolute;
    right: 40px;
    top: 200px;
    display: flex;
    gap: 10px;
    align-items: flex-start;
    text-align: right;
    font-size: 14px;
    line-height: 22px;
    color: var(--navy);
  }
  .address svg { margin-top: 4px; }
</style>
</head>
<body>
  <section class="card card-front" aria-label="Card front">
    <span class="wordmark">KVRo</span>
  </section>

  <section class="card card-back" aria-label="Card back">
    <span class="wordmark">KVRo</span>

    <div class="identity">
      <p class="person-name"><span class="first-name">Daniel</span> <span class="last-name">Hayes</span></p>
      <p class="job-title">Managing Director</p>
    </div>

    <div class="divider"></div>

    <ul class="contact-list">
      <li>
        <svg viewBox="0 0 16 16" fill="var(--orange)"><path d="M3 1h3l1.5 4-2 1.2a9 9 0 0 0 4.3 4.3L11 8.5l4 1.5v3a2 2 0 0 1-2 2A12 12 0 0 1 1 3a2 2 0 0 1 2-2z"/></svg>
        +0 (000)000-0000
      </li>
      <li>
        <svg viewBox="0 0 16 16" fill="none" stroke="var(--orange)" stroke-width="1.6"><rect x="1.5" y="3.5" width="13" height="9"/><path d="M1.5 3.5 8 9l6.5-5.5"/></svg>
        info@yourdomain.com
      </li>
      <li>
        <svg viewBox="0 0 16 16" fill="none" stroke="var(--orange)" stroke-width="1.6"><circle cx="8" cy="8" r="6.5"/><path d="M1.5 8h13M8 1.5c-3 3.5-3 9.5 0 13M8 1.5c3 3.5 3 9.5 0 13"/></svg>
        www.yourdomain.com
      </li>
    </ul>

    <div class="address">
      <p>42 Linden Avenue<br>Carlow 4120</p>
      <svg viewBox="0 0 16 16" fill="var(--orange)"><path d="M8 0a5.5 5.5 0 0 0-5.5 5.5C2.5 10 8 16 8 16s5.5-6 5.5-10.5A5.5 5.5 0 0 0 8 0zm0 7.6a2 2 0 1 1 0-4 2 2 0 0 1 0 4z"/></svg>
    </div>
  </section>
</body>
</html>
```